依頼概要
■依頼目的/概要
Tolino(ブログ)内で「診断レポート」を提供しますので、
表紙デザイン作成をお願いいたします。

■納品物
下記での納品をお願いいたします。
JPEG形式
横1600ピクセル×縦2560ピクセル

■診断レポートの内容
<レポートのタイトル>
40代からのあなたの強みを最大限に生かすための3つの視点 ビジネスもプライベートも充実した人生を手に入れる

<キャッチコピー>
以下の文言の中から組み合わせるか、選んで載せてください。

・他人軸で生きる辛さから脱却しないと人生に悔いが残る!

・人生の転機のヒントが得られる!

・自分らしく生きるヒントが分かる!

・ハンディや持病を抱えながらも一部上場企業に貢献し、独立・起業したコーチが伝える

<著者名>
・著者名 前田芳典(ライフコーチ) M&R 合同会社 代表

■デザイン要望
・本のタイトル/キャッチコピー/著者名の反映をお願い致します。

・読者は40代50代60代の自分らしく生きようとしている人です。

・これからの人生設計を踏まえた考え方や捉え方を書いたレポートですので、
「ビジネス書の表紙」というイメージでお願いします。

・タイトル文字数が、ちょっと多いのですが、
できるだけ文字を認識しやすいようにしたいです。

・未来の人生に新たな可能性が見えるイメージです。

・タイトルの中では、「強み」「充実した人生」「生かす」
あたりが、目立つようにしたいです。

<表現したいイメージなど>
・信頼感
・ビジネス書っぽい感じ
・ベストセラーのマーケティング関連ビジネス書など、
どこかで見たことがあるような感じの安心感
・カラーの希望などはありません。お任せで。

<利用画像について>
イラスト等素材を使用される場合には、
商用利用可の素材をお願いします。

■その他、デザインを考えるのに必要な情報などありましたら、
お答えしますので、遠慮なく聞いて下さい。
■ 選んだ理由

皆様のレベルが高くて本当に嬉しい限りです。選定したポイントは、2案を出してもらいながら、シンプルで分かりやすく、タイトル周りの文字もメリハリがあり、「強み」「生かす」が強調されており、「人生の転機」も目を引き付けました。「充実した人生」も金色で表現しているところにデザインの秀逸さを感じました。また、ビジネス本という視点からも、青白でシンプルに構成され伝わりやすい表現がベストセラーにも多いので、そこにも共感をしました。一部修正依頼をさせていただいた対応も迅速丁寧で感謝しております。

■ 提案者全員のお礼・コメント

皆様、多くの素晴らしいご提案をいただき感謝しております。本当にありがとうございました。次回の依頼する際におきましてもご協力いただきますようお願いいたします。今後ともどうぞよろしくお願いいたします。

```html
<!DOCTYPE html>
<html lang="ja">
<head>
<meta charset="UTF-8">
<title>40代からのあなたの強みを最大限に生かすための3つの視点</title>
<link href="https://fonts.googleapis.com/css2?family=Noto+Sans+JP:wght@500;700;900&display=swap" rel="stylesheet">
<style>
  :root {
    --navy: #0b2f86;
    --blue: #1456c8;
    --bright-blue: #1a63e0;
    --ink: #111111;
    --white: #ffffff;
    --gold: #f2c94c;
  }
  * { margin: 0; padding: 0; box-sizing: border-box; }
  html, body { width: 750px; height: 1200px; overflow: hidden; background: var(--white); }
  body { font-family: "Noto Sans JP", sans-serif; }
  .cover { position: relative; width: 750px; height: 1200px; overflow: hidden; background: var(--white); }

  .top-band {
    position: absolute; left: 0; top: 0; width: 750px; height: 82px;
    background: linear-gradient(90deg, var(--navy), var(--blue));
  }
  .top-band__text {
    position: absolute; left: 22px; top: 10px;
    color: var(--white); font-weight: 700; font-size: 46px; letter-spacing: 1px;
  }

  .title { position: absolute; left: 22px; top: 108px; color: var(--ink); font-weight: 900; line-height: 1; }
  .title__line { display: block; white-space: nowrap; }
  .title__line--sm { font-size: 86px; letter-spacing: -2px; }
  .title__line--lg { font-size: 128px; letter-spacing: -4px; }
  .title__line--xs { font-size: 78px; letter-spacing: -2px; }
  .title__line + .title__line { margin-top: 14px; }

  .points-number {
    position: absolute; left: 505px; top: 108px;
    color: var(--bright-blue); font-weight: 900;
    font-size: 300px; line-height: 0.85; letter-spacing: -6px;
  }
  .points-label {
    position: absolute; left: 618px; top: 405px; width: 76px;
    display: flex; flex-direction: column; align-items: center;
    color: var(--bright-blue); font-weight: 900; line-height: 1;
  }
  .points-label__char { display: block; font-size: 66px; height: 74px; }
  .points-label__char--small { font-size: 52px; height: 60px; }

  .author { position: absolute; right: 22px; top: 728px; color: var(--ink); font-weight: 700; font-size: 23px; line-height: 1.45; }

  .bottom-band {
    position: absolute; left: 0; top: 820px; width: 750px; height: 380px;
    background: linear-gradient(180deg, var(--blue), var(--navy));
  }
  .turning-badge {
    position: absolute; left: 14px; top: 790px; width: 175px; height: 175px;
    border-radius: 50%; background: var(--white); border: 5px solid var(--bright-blue);
    display: flex; flex-direction: column; align-items: center; justify-content: center;
    color: var(--bright-blue); font-weight: 900; font-size: 44px; line-height: 1.15;
  }
  .hint-copy {
    position: absolute; left: 20px; top: 1010px; color: var(--white);
    font-weight: 900; font-size: 38px; line-height: 1.35;
  }
  .life-copy {
    position: absolute; right: 22px; top: 835px; text-align: center; color: var(--white); font-weight: 900;
  }
  .life-copy__line { display: block; font-size: 50px; line-height: 1.2; }
  .life-copy__accent {
    display: block; margin-top: 6px; font-size: 72px; line-height: 1.15; letter-spacing: -1px;
    color: var(--gold);
  }
  .life-copy__tail { display: block; font-size: 46px; line-height: 1.3; }
  .life-copy__tail b { font-size: 62px; }
</style>
</head>
<body>
<main class="cover">
  <header class="top-band"><p class="top-band__text">40代からの</p></header>

  <h1 class="title">
    <span class="title__line title__line--sm">あなたの</span>
    <span class="title__line title__line--lg">強みを</span>
    <span class="title__line title__line--sm">最大限に</span>
    <span class="title__line title__line--lg">生かす</span>
    <span class="title__line title__line--xs">ための</span>
  </h1>

  <div class="points-number">3</div>
  <div class="points-label" aria-label="つの視点">
    <span class="points-label__char points-label__char--small">つ</span>
    <span class="points-label__char points-label__char--small">の</span>
    <span class="points-label__char">視</span>
    <span class="points-label__char">点</span>
  </div>

  <p class="author">著者&nbsp; 前田芳典 (ライフコーチ)<br>M&amp;R 合同会社 代表</p>

  <section class="bottom-band"></section>

  <div class="turning-badge"><span>人生の</span><span>転機</span></div>

  <p class="hint-copy">自分らしく<br>生きるヒント<br>が分かる!</p>

  <p class="life-copy">
    <span class="life-copy__line">ビジネスも</span>
    <span class="life-copy__line">プライベートも</span>
    <span class="life-copy__accent">充実した人生</span>
    <span class="life-copy__tail"><b>を</b>手に入れる</span>
  </p>
</main>
</body>
</html>
```